Copper Lantern Fitness Flyer

We need a Flyer designed for a Revolutionary Fresh New Functional Fitness facility in Manly Sydney, Australia. We have just recently opened and now need to get the word out. Using the flyers to hand out at events also for shop counters and letterbox drops.

Our company name is Copper Lantern Fitness "Where STRENGTH Becomes Your SPARK".
We promote health and fitness to all fitness levels concentrating on functional fitness. To learn more about us and our colour scheme see attached file and also check us out on www.brightvine-social.example/copperlanternfitnessgroup

A5 Size please

Target Market(s)

The beauty of our system is it is for everyone we have girls and guys in there teens, 20's 30's 40's and 50's. Not only that we have professional athletes, military and high fitness levels all the way to people who are overweight and need to loose weight and tone up. The system caters for everyone.

Industry/Entity Type

Fitness

Requirements
Must have
• FRONT:

Free 30min Fat Blasting Experience With Your Very Own Personal Trainer !!!

New Class Starts Every 3 minutes.
30 minute Workout With A Trainer.
No Machines No Mirrors And No Attitudes.
Catering For All Fitness Levels.
Results Guaranteed Or Your Money Back.
Fun, Fresh, Clean, Revolutionary New Facility.

Back:

You Are Just Moments Away From Burning Fat Faster Than Ever Before And Getting That Body You Always Wanted !!!

Come In Today To Claim Your FREE Workout.

Ph (02) 9417 2086
Address 5/127 Greywattle Ave Fernbrook 2178
www.brightvine-social.example/copperlanternfitnessgroup
Nice to have
• FRONT:

Back:

Ph (02) 9417 2086

```html
<!DOCTYPE html>
<html lang="en">
<head>
<meta charset="utf-8">
<title>Copper Lantern Fitness Flyer</title>
<link href="https://fonts.googleapis.com/css2?family=Oswald:wght@300;400;500;600&family=Roboto+Condensed:wght@400;700&display=swap" rel="stylesheet">
<style>
  :root {
    --stage: #3d3d3d;
    --ink: #050505;
    --yellow: #f5ec1a;
    --blue: #1d8fd0;
    --red: #e63a2e;
    --white: #ffffff;
    --gold: #c9a640;
  }
  * { margin: 0; padding: 0; box-sizing: border-box; }
  html, body { width: 1200px; height: 1000px; overflow: hidden; }
  body { background: var(--stage); position: relative; font-family: "Roboto Condensed", sans-serif; }

  .flyer { position: absolute; background: var(--ink); overflow: hidden; box-shadow: 4px 4px 8px rgba(0,0,0,.55); }
  .flyer--front { left: 52px; top: 32px; width: 650px; height: 462px; }
  .flyer--back { left: 502px; top: 510px; width: 650px; height: 460px; }

  .photo { position: absolute; }
  .photo--athletes { left: 0; top: 0; width: 270px; height: 462px;
    background:
      linear-gradient(90deg, rgba(5,5,5,0) 0%, rgba(5,5,5,0) 72%, var(--ink) 100%),
      linear-gradient(180deg, #2b95b0 0%, #8a6048 14%, #9a5a3a 40%, #7a4a30 70%, #5f6b4e 88%, #1a1a1a 100%); }
  .photo--gym { left: 230px; top: 248px; width: 420px; height: 214px;
    background:
      linear-gradient(90deg, rgba(5,5,5,0.95) 0%, rgba(5,5,5,0) 18%),
      linear-gradient(180deg, #6e7478 0%, #4a4f52 45%, #2c2f31 100%); }

  .headline { position: absolute; right: 36px; text-align: right; font-family: "Oswald", sans-serif; }
  .headline--free { top: 30px; font-size: 60px; line-height: 60px; font-weight: 500; color: var(--yellow); letter-spacing: 2px; }
  .headline--blast { top: 80px; font-size: 32px; line-height: 34px; font-weight: 500; color: var(--blue); letter-spacing: 1px; }
  .headline--trainer { top: 114px; font-family: "Roboto Condensed", sans-serif; font-size: 15.5px; line-height: 18px; color: var(--white); }

  .benefits { position: absolute; left: 243px; top: 134px; width: 407px; height: 108px; padding: 6px 36px 0 0;
    background: linear-gradient(90deg, rgba(230,58,46,0) 0%, var(--red) 28%, var(--red) 100%);
    list-style: none; text-align: right; }
  .benefits li { font-size: 12.5px; line-height: 16px; font-weight: 700; color: var(--white); }
  .benefits li:nth-child(even) { color: var(--yellow); }

  .brand-panel { position: absolute; left: 476px; top: 262px; width: 168px; height: 198px;
    background: var(--ink); border: 1px solid var(--blue);
    display: flex; flex-direction: column; align-items: center; justify-content: center; gap: 14px; }
  .brand-panel__mark { width: 30px; height: 30px; background: var(--gold); }
  .brand-panel__name { font-family: "Oswald", sans-serif; font-weight: 500; font-size: 18px; line-height: 21px;
    color: var(--gold); text-align: center; text-transform: uppercase; }

  .back-banner { position: absolute; left: 0; top: 0; width: 650px; height: 120px; }
  .back-banner__text { position: absolute; left: 40px; top: 29px; font-size: 17.5px; line-height: 22px;
    font-weight: 700; color: var(--white); }

  .photo--glutes { left: 300px; top: 70px; width: 350px; height: 390px;
    background: linear-gradient(90deg, var(--ink) 0%, #1a1410 22%, #5a3522 40%, #171717 55%, #222 80%, #4a2c1c 100%); }

  .cta { position: absolute; left: 40px; font-family: "Oswald", sans-serif; }
  .cta--today { top: 118px; font-size: 37px; line-height: 44px; font-weight: 500; color: var(--red); }
  .cta--claim { top: 160px; font-size: 27px; line-height: 30px; font-weight: 500; color: var(--blue); letter-spacing: 3.5px; }
  .cta--free { top: 178px; font-size: 132px; line-height: 132px; font-weight: 600; color: var(--yellow); letter-spacing: 1px; }
  .cta--workout { top: 286px; font-size: 61px; line-height: 64px; font-weight: 300; color: var(--blue); letter-spacing: 1px; }

  .contact { position: absolute; left: 0; top: 358px; width: 340px; height: 68px; padding: 15px 0 0 42px;
    background: linear-gradient(90deg, var(--red) 0%, var(--red) 86%, rgba(230,58,46,0) 100%); }
  .contact p { font-size: 10px; line-height: 13px; font-weight: 700; color: var(--white); white-space: nowrap; }
  .contact span { color: var(--yellow); }
</style>
</head>
<body>

<section class="flyer flyer--front" aria-label="Flyer front">
  <div class="photo photo--athletes" role="img" aria-label="Photo of a toned woman's midriff above a muscular man lifting dumbbells"></div>
  <div class="photo photo--gym" role="img" aria-label="Photo of the functional training gym floor with bags and equipment"></div>

  <h1 class="headline headline--free">FREE 30MIN</h1>
  <h2 class="headline headline--blast">FAT BLASTING EXPERIENCE</h2>
  <p class="headline headline--trainer">WITH YOUR VERY OWN PERSONAL TRAINER!</p>

  <ul class="benefits">
    <li>New Class Starts Every 3 minutes.</li>
    <li>30 minute Workout With A Trainer.</li>
    <li>No Machines No Mirrors And No Attitudes.</li>
    <li>Catering For All Fitness Levels.</li>
    <li>Results Guaranteed Or Your Money Back.</li>
    <li>Fun, Fresh, Clean, Revolutionary New Facility.</li>
  </ul>

  <div class="brand-panel">
    <div class="brand-panel__mark"></div>
    <p class="brand-panel__name">Copper Lantern<br>Fitness</p>
  </div>
</section>

<section class="flyer flyer--back" aria-label="Flyer back">
  <div class="photo photo--glutes" role="img" aria-label="Photo of a woman in black shorts holding a dumbbell"></div>

  <svg class="back-banner" width="650" height="120" viewBox="0 0 650 120" aria-hidden="true">
    <polygon points="0,0 650,0 650,68 0,98" fill="#1d8fd0"/>
    <polygon points="0,98 650,68 650,76 0,116" fill="#e63a2e"/>
  </svg>
  <p class="back-banner__text">You Are Just Moments Away From Burning Fat Faster Than Ever Before<br>And Getting That Body You Always Wanted !!!</p>

  <p class="cta cta--today">COME IN TODAY</p>
  <p class="cta cta--claim">TO CLAIM YOUR</p>
  <p class="cta cta--free">FREE</p>
  <p class="cta cta--workout">WORKOUT</p>

  <div class="contact">
    <p><span>Ph</span> (02) 9417 2086</p>
    <p><span>Address</span> 5/127 Greywattle Ave Fernbrook 2178</p>
    <p>www.brightvine-social.example/copperlanternfitnessgroup</p>
  </div>
</section>

</body>
</html>
```